Orva Business Card

we need a business card for flooring business called Orva Flooring, the design should be black and white. we have 2 locations

Harlowvale Showroom
527 Kellerman Road,
Harlowvale VIC 3952

Ashdene Showroom
462 Bramwell Hwy,
Ashdene VIC 3968

email : sales@orvaflooring.com.au
(03) 9471 2830

Please inform we sell , Laminate, Hybrid, Timber, carpet and commercial flooring

```html
<!DOCTYPE html>
<html lang="en">
<head>
<meta charset="utf-8">
<title>Orva Flooring Business Card</title>
<link href="https://fonts.googleapis.com/css2?family=Arimo:wght@400;700&display=swap" rel="stylesheet">
<style>
  :root {
    --backdrop: #d4d4d4;
    --card: #333333;
    --ink: #ffffff;
    --ink-soft: #e6e6e6;
    --band: #ffffff;
    --band-ink: #333333;
    --rule: #d0d0d0;
  }
  * { margin: 0; padding: 0; box-sizing: border-box; }
  html, body {
    width: 1200px; height: 801px; overflow: hidden;
    background: var(--backdrop);
    font-family: "Arimo", Arial, sans-serif;
  }
  .stage {
    width: 1200px; height: 801px;
    display: flex; align-items: center; justify-content: center; gap: 50px;
  }
  .card {
    position: relative;
    width: 540px; height: 330px;
    background: var(--card);
    border-radius: 22px;
    overflow: hidden;
    color: var(--ink);
  }
  .person { position: absolute; left: 40px; top: 62px; }
  .person-name { font-size: 21px; font-weight: 700; letter-spacing: 0.5px; text-transform: uppercase; }
  .person-role { font-size: 15px; margin-top: 3px; color: var(--ink-soft); }
  .brand-name {
    position: absolute; right: 40px; top: 58px;
    font-size: 31px; font-weight: 400; letter-spacing: 1px;
    display: flex; align-items: center; gap: 10px;
  }
  .brand-dot { width: 12px; height: 12px; border-radius: 50%; background: var(--ink); }
  .contact { position: absolute; left: 40px; top: 150px; font-size: 15px; line-height: 23px; }
  .contact-row { display: flex; align-items: center; gap: 8px; }
  .contact-row svg { width: 13px; height: 13px; flex: none; }
  .divider {
    position: absolute; left: 40px; right: 40px; top: 202px;
    height: 1px; background: var(--rule);
  }
  .showroom { position: absolute; top: 214px; font-size: 14px; line-height: 19px; }
  .showroom-left { left: 40px; }
  .showroom-right { right: 40px; }
  .showroom-title { font-weight: 700; font-size: 15px; }
  .band-rule {
    position: absolute; left: 0; right: 0; top: 284px;
    height: 1px; background: var(--rule);
  }
  .services-band {
    position: absolute; left: 0; right: 0; bottom: 0; height: 38px;
    background: var(--band); color: var(--band-ink);
    display: flex; align-items: center; justify-content: center;
    font-size: 16px; letter-spacing: 0.2px;
  }
  .card-back { display: flex; align-items: center; justify-content: center; }
  .back-name {
    font-size: 56px; font-weight: 400; letter-spacing: 2px;
    display: flex; align-items: center; gap: 18px;
  }
  .back-name .brand-dot { width: 20px; height: 20px; }
</style>
</head>
<body>
<main class="stage">
  <section class="card card-front">
    <div class="person">
      <div class="person-name">Marcus Hale</div>
      <div class="person-role">Manager</div>
    </div>
    <div class="brand-name"><span class="brand-dot"></span>Orva Flooring</div>
    <div class="contact">
      <div class="contact-row">
        <svg viewBox="0 0 16 16" aria-hidden="true"><path fill="#fff" d="M3.5 1.5l2.4 2.8-1.3 1.6c.8 2 2.5 3.7 4.5 4.5l1.6-1.3 2.8 2.4-1.5 2.3C7 13.5 2.5 9 1.2 3z"/></svg>
        <span>(03) 9471 2830</span>
      </div>
      <div class="contact-row">
        <svg viewBox="0 0 16 16" aria-hidden="true"><rect x="1.5" y="3.5" width="13" height="9" fill="none" stroke="#fff" stroke-width="1.4"/><path d="M1.5 3.5L8 9l6.5-5.5" fill="none" stroke="#fff" stroke-width="1.4"/></svg>
        <span>sales@orvaflooring.com.au</span>
      </div>
    </div>
    <div class="divider"></div>
    <div class="showroom showroom-left">
      <div class="showroom-title">Harlowvale Showroom</div>
      <div>527 Kellerman Road,</div>
      <div>Harlowvale VIC 3952</div>
    </div>
    <div class="showroom showroom-right">
      <div class="showroom-title">Ashdene Showroom</div>
      <div>462 Bramwell Hwy,</div>
      <div>Ashdene VIC 3968</div>
    </div>
    <div class="band-rule"></div>
    <div class="services-band">• Laminate • Hybrid • Timber • carpet • commercial flooring</div>
  </section>

  <section class="card card-back">
    <div class="back-name"><span class="brand-dot"></span>Orva Flooring</div>
  </section>
</main>
</body>
</html>
```